Business Card

Yes I would like you to design me a business card with the logo you just made me

Industry/Entity Type

Business

Colors
33b7a4
00a990
333333
000000
757575
7f7f7f

```html
<!DOCTYPE html>
<html lang="en">
<head>
<meta charset="utf-8">
<title>Lena Marvik Photography – Business Card</title>
<link rel="stylesheet" href="https://fonts.googleapis.com/css2?family=Hind:wght@500;600&family=Montserrat:wght@700&display=swap">
<style>
  :root {
    --page: #ffffff;
    --bleed: #d1d2d4;
    --crop: #6d6e71;
    --card: #ffffff;
    --blue: #1fa5dc;
    --green: #00a990;
    --teal: #12b7a2;
    --ink: #333333;
    --mark: #2a2b2d;
  }
  * { margin: 0; padding: 0; box-sizing: border-box; }
  html, body { width: 1200px; height: 1000px; overflow: hidden; background: var(--page); }
  .sheet { position: relative; width: 1200px; height: 1000px; }
  .artwork { position: absolute; inset: 0; }
  .contact-list {
    position: absolute; left: 362px; top: 92px; list-style: none;
    font-family: "Hind", sans-serif; font-weight: 500; font-size: 17px;
    color: var(--ink); letter-spacing: 0.2px;
  }
  .contact-list li { height: 29px; line-height: 24px; }
  .person {
    position: absolute; left: 356px; top: 304px; width: 200px; text-align: center;
    font-family: "Hind", sans-serif;
  }
  .person-name {
    font-family: "Montserrat", sans-serif; font-weight: 700; font-size: 23px;
    color: var(--green); line-height: 30px;
  }
  .person-role { font-weight: 500; font-size: 17px; color: var(--ink); line-height: 20px; }
  .brand-name {
    position: absolute; text-align: center;
    font-family: "Hind", sans-serif; font-weight: 500; color: var(--ink);
  }
  .brand-name--front { left: 600px; top: 302px; width: 270px; font-size: 30px; line-height: 32px; }
  .brand-name--back { left: 440px; top: 770px; width: 310px; font-size: 36px; line-height: 38px; }
</style>
</head>
<body>
<main class="sheet">
  <svg class="artwork" width="1200" height="1000" viewBox="0 0 1200 1000" aria-hidden="true">
    <!-- front side -->
    <g class="card-front">
      <rect x="300" y="28" width="602" height="404" fill="var(--bleed)"/>
      <rect x="319" y="47" width="563" height="364" rx="18" fill="var(--card)"/>
      <clipPath id="front-clip"><rect x="319" y="47" width="563" height="364" rx="18"/></clipPath>
      <g clip-path="url(#front-clip)">
        <polygon points="319,47 353,47 353,263 319,283" fill="var(--blue)"/>
        <polygon points="319,283 353,263 353,411 319,411" fill="var(--green)"/>
        <line x1="319" y1="284" x2="353" y2="264" stroke="#ffffff" stroke-width="3"/>
      </g>
      <g class="contact-icons" fill="none" stroke="#ffffff" stroke-width="1.6">
        <circle cx="336" cy="103" r="10"/>
        <path d="M331 98 q1 8 9 10 l1.5-2.5 -3-1.5 -1.5 1.5 q-3-1.5-4-4 l1.5-1.5 -1.5-3z" fill="#ffffff" stroke="none"/>
        <circle cx="336" cy="132" r="10"/>
        <rect x="330" y="128" width="12" height="8"/>
        <path d="M330 128 l6 5 6-5"/>
        <circle cx="336" cy="161" r="10"/>
        <circle cx="336" cy="161" r="6"/>
        <path d="M330 161 h12 M336 155 v12 M331 158 h10 M331 164 h10"/>
        <circle cx="336" cy="190" r="10"/>
        <circle cx="336" cy="190" r="5" fill="#ffffff" stroke="none"/>
      </g>
      <circle class="brand-dot" cx="723" cy="267" r="28" fill="var(--mark)"/>
    </g>
    <!-- back side -->
    <g class="card-back">
      <rect x="300" y="557" width="602" height="404" fill="var(--bleed)"/>
      <rect x="319" y="577" width="563" height="364" rx="18" fill="var(--teal)"/>
      <circle class="brand-dot" cx="595" cy="726" r="33" fill="var(--mark)"/>
    </g>
    <!-- crop marks -->
    <g class="crop-marks" stroke="var(--crop)" stroke-width="1">
      <path d="M319 0 V47 M882 0 V47 M319 411 V472 M882 411 V472 M270 47 H319 M882 47 H932 M270 411 H319 M882 411 H932"/>
      <path d="M319 532 V577 M882 532 V577 M319 941 V1000 M882 941 V1000 M270 577 H319 M882 577 H932 M270 941 H319 M882 941 H932"/>
    </g>
  </svg>

  <ul class="contact-list">
    <li>555-210-4836</li>
    <li>lenamarvikphoto@mail.com</li>
    <li>www.lenamarvikphoto.com</li>
    <li>social.example/lenamarvikphotography</li>
  </ul>

  <div class="person">
    <p class="person-name">Lena Marvik</p>
    <p class="person-role">Photographer</p>
  </div>

  <p class="brand-name brand-name--front">Lena Marvik<br>Photography</p>
  <p class="brand-name brand-name--back">Lena Marvik<br>Photography</p>
</main>
</body>
</html>
```